Tovira Botanics Website Revamping for Ecommerce

Looking to upgrade our website and provide a better experience to users both visually and from a navigation standpoint. Here is our current site

http://toviraleafworks dot com/

Below are some Shopify Design Concepts We Like.
https://lumbergloss. com/pages/classic
https://www.korvabites. com/
https://www.quillmarrowfen. com/

Target Market(s)

People with Darker Skin Tone (Black and Brown)

Industry/Entity Type

Skin Care Product

Number of Pages Required

4 page

Requirements
Must have
• Use the Brand Guide
Nice to have
• Focus on E-Commerce Platforms such as Shopify but can be other platforms too
Should not have
• Don't deviate from Brand Guide (Attached)

```html
<!DOCTYPE html>
<html lang="en">
<head>
<meta charset="utf-8">
<title>Tovira Botanics</title>
<link href="https://fonts.googleapis.com/css2?family=Montserrat:wght@400;500;600;700&family=Open+Sans:wght@400;600&display=swap" rel="stylesheet">
<style>
:root{
  --green:#3c9f47;
  --green-dark:#2f8a3b;
  --leaf-soft:#dcebc9;
  --ink:#2d2d2d;
  --muted:#8a8a8a;
  --hero-grey:#b9b8b4;
  --star:#3c9f47;
  --white:#ffffff;
}
*{margin:0;padding:0;box-sizing:border-box}
html,body{width:1200px;height:2820px;overflow:hidden;background:var(--white)}
body{position:relative;font-family:"Open Sans",sans-serif;color:var(--ink)}
.abs{position:absolute}

.topbar{left:0;top:0;width:1200px;height:28px;background:var(--green);color:var(--white);font:600 10px "Montserrat",sans-serif;letter-spacing:.5px;display:flex;align-items:center;justify-content:space-between;padding:0 40px}
.social{display:flex;gap:14px}
.social span{width:10px;height:10px;border-radius:50%;background:rgba(255,255,255,.85)}

.brand{left:0;top:60px;width:1200px;text-align:center}
.brand .mark{display:inline-block;width:18px;height:18px;border-radius:50%;background:var(--green);margin-bottom:4px}
.brand .name{font:500 62px "Montserrat",sans-serif;color:var(--green);letter-spacing:1px;line-height:1}
.nav{left:0;top:198px;width:1200px;display:flex;justify-content:center;gap:46px;font:600 11px "Montserrat",sans-serif;letter-spacing:.6px;color:var(--ink)}
.nav .icons{display:flex;gap:10px;align-items:center}
.nav .icons i{display:block;width:10px;height:10px;border-radius:50%;background:var(--green)}

.hero{left:0;top:232px;width:1200px;height:508px;background:linear-gradient(90deg,#8f8e8a 0%,var(--hero-grey) 45%,#d6b27a 72%,#c99a48 100%)}
.hero h1{left:40px;top:140px;font:600 40px/1.35 "Montserrat",sans-serif;color:var(--white);letter-spacing:3px}
.badges{left:90px;top:360px;display:flex;gap:32px}
.badges span{width:66px;height:66px;border-radius:50%;background:rgba(255,255,255,.35);border:3px solid rgba(255,255,255,.6)}
.badges span:first-child{background:#c23b3b;border-color:#e6e6e6}
.badges span:nth-child(2){background:#2f7f3a;border-color:#e6e6e6}

.leaves-left{left:0;top:740px;width:150px;height:1830px;background:linear-gradient(90deg,var(--leaf-soft),rgba(220,235,201,0))}
.leaves-right{right:0;top:740px;width:150px;height:1830px;background:linear-gradient(270deg,var(--leaf-soft),rgba(220,235,201,0))}

.section-title{left:0;width:1200px;text-align:center;font:600 26px "Montserrat",sans-serif;color:var(--green);letter-spacing:2px}

.product{width:200px;top:880px;text-align:left}
.product .bottle{height:236px;margin:0 auto 14px;width:90px;border-radius:14px 14px 8px 8px;background:linear-gradient(180deg,#1f6b2c,#3aa04a 60%,#2b7c36)}
.product .bottle.bundle{width:170px;background:linear-gradient(90deg,#2b7c36 0 30%,transparent 30% 35%,#3aa04a 35% 65%,transparent 65% 70%,#2b7c36 70%)}
.product .title{font:600 12px "Montserrat",sans-serif;letter-spacing:.4px}
.product .meta{display:flex;justify-content:space-between;margin-top:10px;font:600 16px "Montserrat",sans-serif}
.product .stars{color:var(--star);font-size:15px;letter-spacing:1px}

.ingredient{width:1200px;left:0}
.ingredient h3{font:600 32px "Montserrat",sans-serif;color:var(--ink);margin-bottom:12px}
.ingredient p{font:400 13px/1.7 "Open Sans",sans-serif;color:var(--muted);width:500px}
.ingredient .text{position:absolute}
.ingredient .art{position:absolute;width:90px;height:90px;border-radius:50%}

.press{left:0;top:2440px;width:1200px;display:flex;justify-content:space-around;padding:0 170px;align-items:center;font:700 26px "Montserrat",sans-serif;color:var(--ink)}

.scenery{left:0;top:2560px;width:1200px;height:220px;background:linear-gradient(180deg,rgba(255,255,255,0),#a9d27a 55%,#5aa63c)}
.footer{left:0;top:2780px;width:1200px;height:40px;background:var(--green-dark);color:var(--white);font:400 10px "Open Sans",sans-serif;display:flex;align-items:center;justify-content:center}
.footer .lang{position:absolute;right:40px}
</style>
</head>
<body>
<div class="abs topbar"><span>FREE SHIPPING OVER $50 (USA)</span><div class="social"><span></span><span></span><span></span><span></span><span></span></div></div>

<div class="abs brand"><div class="mark"></div><div class="name">tovira</div></div>
<nav class="abs nav"><span>HOME</span><span>SHOP</span><span>ABOUT US</span><span>GO NATURAL</span><span>CONTACT US</span><span class="icons"><i></i><i></i></span></nav>

<section class="abs hero" role="img" aria-label="Smiling woman with curly hair in a yellow top against a grey backdrop">
  <h1 class="abs">PAMPER YOUR SKIN<br>WITH TOVIRA</h1>
  <div class="abs badges"><span></span><span></span><span></span></div>
</section>

<div class="abs leaves-left" role="img" aria-label="Soft green leaf border"></div>
<div class="abs leaves-right" role="img" aria-label="Soft green leaf border"></div>

<h2 class="abs section-title" style="top:795px">OUR PRODUCTS</h2>
<div class="abs product" style="left:120px"><div class="bottle" role="img" aria-label="Green toner bottle"></div><div class="title">PURIFYING TONER LOTION</div><div class="meta"><span>$12.99</span><span class="stars">★★★★★</span></div></div>
<div class="abs product" style="left:360px"><div class="bottle" role="img" aria-label="Green cream pump bottle"></div><div class="title">FACIAL CREAM</div><div class="meta"><span>$19.99</span><span class="stars">★★★★★</span></div></div>
<div class="abs product" style="left:600px"><div class="bottle" role="img" aria-label="Green body lotion bottle"></div><div class="title">BODY LOTION</div><div class="meta"><span>$15.99</span><span class="stars">★★★★★</span></div></div>
<div class="abs product" style="left:860px"><div class="bottle bundle" role="img" aria-label="Three green bottles bundle"></div><div class="title">TOVIRA BUNDLE</div><div class="meta"><span>$45.00</span><span class="stars">★★★★★</span></div></div>

<h2 class="abs section-title" style="top:1275px">AMAZING INGREDIENTS</h2>

<div class="abs ingredient" style="top:1390px">
  <div class="art" style="left:320px;top:0;background:radial-gradient(circle,#9b86c9,rgba(155,134,201,0) 70%)" role="img" aria-label="Lavender sprig"></div>
  <div class="text" style="left:490px;top:0"><h3>Lavender</h3><p>Lavender has antiseptic and anti-inflammatory properties. It inhibits the growth of bacteria by fighting against the harmful effects of pollutants on the skin.</p></div>
</div>
<div class="abs ingredient" style="top:1570px">
  <div class="text" style="left:230px;top:0"><h3>Green Tea</h3><p>Green tea improves your skin complexion and makes your skin healthy. It helps flush out toxins from the skin, heals blemishes and scars, and reduces inflammation. It also improves skin elasticity.</p></div>
  <div class="art" style="left:820px;top:20px;background:radial-gradient(circle,#3f9a3a,rgba(63,154,58,0) 70%)" role="img" aria-label="Green tea leaves"></div>
</div>
<div class="abs ingredient" style="top:1750px">
  <div class="art" style="left:300px;top:10px;background:radial-gradient(circle,#f29a1e,rgba(242,154,30,0) 70%)" role="img" aria-label="Orange citrus fruit"></div>
  <div class="text" style="left:490px;top:0"><h3>Citrus</h3><p>Citrus helps in softening dry and patched skin. The antioxidants present in citrus speed up cell turnover and also remove dead skin cells.</p></div>
</div>
<div class="abs ingredient" style="top:1935px">
  <div class="text" style="left:230px;top:0"><h3>Jojoba-oil</h3><p>Jojoba oil modulates the sebum production, thereby reducing oiliness. It also acts as an anti-inflammatory agent, soothing the irritated skin.</p></div>
  <div class="art" style="left:830px;top:10px;background:radial-gradient(circle,#a9a55a,rgba(169,165,90,0) 70%)" role="img" aria-label="Jojoba seeds on a branch"></div>
</div>
<div class="abs ingredient" style="top:2125px">
  <div class="art" style="left:290px;top:0;width:110px;height:60px;background:radial-gradient(ellipse,#2f6e28,rgba(47,110,40,0) 70%)" role="img" aria-label="Cucumber"></div>
  <div class="text" style="left:490px;top:0"><h3>Cucumber</h3><p>Cucumber contains phytochemicals that enhance production of collagen, the fiber-like protein responsible for skin elasticity.</p></div>
</div>

<h2 class="abs section-title" style="top:2335px">PEOPLE ARE TALKING</h2>
<div class="abs press"><span>Marlowe</span><span>Brindle</span><span>Kestrel</span><span>Vellane</span></div>

<div class="abs scenery" role="img" aria-label="Green trees and grass landscape"></div>
<footer class="abs footer"><span>© 2017 Tovira. All Rights Reserved</span><span class="lang">USD</span></footer>
</body>
</html>
```